Social Media Post – Promotion Announcement for Dale Renner

Objective:
Create a professional and eye-catching social media post announcing the promotion of Dale Renner to Vice President of Sales – Foodservice. The design should be modern, clean, and aligned with Brenwick Sales & Marketing’s branding style (friendly, West Coast, professional). It should match our website:

www.brenwicksales.example

Key Requirements:

Include Dale Renner’s photo (we will provide a high-resolution image).
Prominently display his name: “Dale Renner.”
Prominently display his new title: “Vice President of Sales – Foodservice.”

A header or highlight that says something like: “Promotion Announcement” or “Congratulations!”

Design must be editable in Canva so we can reuse the template for future promotions.

Square format (1080x1080px) for Instagram/LinkedIn, but adaptable to landscape (1200x628px) if possible.

Style Guide / Preferences:

Colors: Incorporate Brenwick Sales & Marketing brand blue (#0B64C0) along with white, gray, and/or complementary tones.

Fonts: Clean, modern sans-serif. Readable even on mobile.

Layout: Balanced between photo and text.

Option 1: Circular frame for the photo at center/top, text below.

Option 2: Split design with photo on one side and text on the other.

Tone: Professional, celebratory, approachable.

Deliverables:

Canva template file (editable).

Exported PNG/JPEG preview for review.

```html
<!DOCTYPE html>
<html lang="en">
<head>
<meta charset="utf-8">
<title>Promotion Announcement – Dale Renner</title>
<link rel="stylesheet" href="https://fonts.googleapis.com/css2?family=Barlow+Condensed:wght@500;700&family=Montserrat:wght@700;800&display=swap">
<style>
  :root {
    --brand-blue: #0b64c0;
    --brand-blue-deep: #0a4fa3;
    --gold: #fbbd1a;
    --gold-light: #ffe9a8;
    --ink: #454545;
    --white: #ffffff;
  }
  * { margin: 0; padding: 0; box-sizing: border-box; }
  html, body { width: 1200px; height: 1200px; overflow: hidden; background: var(--white); }
  .post {
    position: relative;
    width: 1200px;
    height: 1200px;
    overflow: hidden;
    background: var(--white);
  }
  .backdrop { position: absolute; inset: 0; }
  .headline {
    position: absolute;
    left: 30px;
    top: 26px;
    font-family: "Barlow Condensed", sans-serif;
    font-weight: 500;
    font-size: 82px;
    line-height: 0.95;
    letter-spacing: 1px;
  }
  .headline .kicker { color: var(--gold); display: block; }
  .headline .main { color: var(--white); display: block; }
  .company {
    position: absolute;
    right: 36px;
    top: 32px;
    text-align: center;
    color: var(--white);
    font-family: "Montserrat", sans-serif;
    font-weight: 800;
  }
  .company .company-name { display: block; font-size: 40px; letter-spacing: 1px; line-height: 1.05; }
  .company .company-line { display: block; font-size: 15px; letter-spacing: 4px; margin-top: 6px; }
  .portrait-frame { position: absolute; left: 0; top: 0; }
  .person-name {
    position: absolute;
    left: 0;
    right: 0;
    top: 850px;
    text-align: center;
    font-family: "Barlow Condensed", sans-serif;
    font-weight: 700;
    font-size: 184px;
    line-height: 1;
    color: var(--ink);
    letter-spacing: 4px;
  }
  .role {
    position: absolute;
    left: 0;
    right: 0;
    top: 1030px;
    text-align: center;
    font-family: "Montserrat", sans-serif;
    font-weight: 800;
    color: var(--brand-blue);
    font-size: 61px;
    line-height: 1.1;
  }
  .role .title { display: block; }
  .role .division {
    display: flex;
    align-items: center;
    justify-content: center;
    gap: 40px;
  }
  .role .division::before,
  .role .division::after {
    content: "";
    width: 162px;
    height: 4px;
    background: var(--brand-blue);
  }
</style>
</head>
<body>
<main class="post">
  <svg class="backdrop" width="1200" height="1200" viewBox="0 0 1200 1200">
    <defs>
      <linearGradient id="blue-field" x1="0" y1="0" x2="0" y2="1">
        <stop offset="0" stop-color="#0b64c0"/>
        <stop offset="1" stop-color="#0a4fa3"/>
      </linearGradient>
      <linearGradient id="gold-ribbon" x1="0" y1="0" x2="1" y2="0">
        <stop offset="0" stop-color="#fbbd1a"/>
        <stop offset="0.18" stop-color="#fde08a"/>
        <stop offset="0.3" stop-color="#fbbd1a"/>
        <stop offset="0.72" stop-color="#fbbd1a"/>
        <stop offset="0.86" stop-color="#fff1c4"/>
        <stop offset="1" stop-color="#fbbd1a"/>
      </linearGradient>
    </defs>
    <path class="ribbon" fill="url(#gold-ribbon)"
      d="M0 520 C200 545 400 500 600 420 C820 330 980 200 1200 168 V360 C1000 365 820 420 620 560 C440 690 220 780 0 775 Z"/>
    <path class="ribbon-highlight" fill="#ffffff" opacity="0.5"
      d="M0 735 C220 745 430 670 620 545 C820 410 1000 350 1200 340 V360 C1000 365 820 420 620 560 C440 690 220 780 0 775 Z"/>
    <path class="blue-field" fill="url(#blue-field)"
      d="M0 0 H1200 V168 C980 200 820 330 600 420 C400 500 200 545 0 520 Z"/>
  </svg>

  <h1 class="headline">
    <span class="kicker">PROMOTION</span>
    <span class="main">ANNOUNCEMENT</span>
  </h1>

  <div class="company">
    <span class="company-name">BRENWICK</span>
    <span class="company-line">Sales &amp; Marketing</span>
  </div>

  <svg class="portrait-frame" width="1200" height="1200" viewBox="0 0 1200 1200">
    <defs>
      <linearGradient id="ring-gold" x1="0" y1="0" x2="1" y2="1">
        <stop offset="0" stop-color="#f9b200"/>
        <stop offset="0.55" stop-color="#fde07a"/>
        <stop offset="1" stop-color="#f7b100"/>
      </linearGradient>
      <radialGradient id="portrait-tone" cx="0.5" cy="0.42" r="0.6">
        <stop offset="0" stop-color="#e3c2b4"/>
        <stop offset="0.45" stop-color="#f3f3f3"/>
        <stop offset="0.8" stop-color="#ffffff"/>
        <stop offset="1" stop-color="#6a4a3a"/>
      </radialGradient>
    </defs>
    <circle class="ring" cx="600" cy="530" r="316" fill="url(#ring-gold)"/>
    <circle class="ring-inner" cx="600" cy="530" r="290" fill="#ffe9a8"/>
    <circle class="portrait" cx="600" cy="530" r="282" fill="url(#portrait-tone)"
      role="img" aria-label="Headshot of Dale Renner in a brown blazer and checked shirt"/>
  </svg>

  <h2 class="person-name">DALE RENNER</h2>
  <p class="role">
    <span class="title">VICE PRESIDENT OF SALES</span>
    <span class="division">FOODSERVICE</span>
  </p>
</main>
</body>
</html>
```